Business Card for Managing Partner Investment Fund

To create a business card template for an investment fund manager. Business card should be more professional in nature, not too colorful, more upscale, and created using the attached logos and fund name files. I would prefer a black or gray color scheme, but am open to the use of color as well. I would prefer a double sided business card, but open to single sided business card designs as well. The business card should include: name, title, and contact information, as well as logo and company name. I would prefer a more stream-lined, simple business card design.
Updates
Address: 4190 NE 38th Ter. Ocala, FL 34470
Email: talvin47@quorimail.net
Phone: 561-347-9162
Title: managing partner
Name: Dorian Velsky
Fund Name: Ambergate Capital
Logos can be found in files attached to the brief
Target Market(s)
potential investors, other fund managers
Industry/Entity Type
Finance
Contact Information for Business Card
Name on card: Dorian Velsky
Title: Managing Partner
Colors
Designer to choose colors to be used in the design.
Requirements
Must have
- Phone number
- email address
- physical address
- title
- name
- logo
- Fund name
Nice to have
- simple layout
Should not have
- too many colors, busy fonts,

```html
<!DOCTYPE html>
<html lang="en">
<head>
<meta charset="utf-8">
<title>Ambergate Capital – Business Card</title>
<link rel="stylesheet" href="https://fonts.googleapis.com/css2?family=Cinzel:wght@400;600&display=swap">
<style>
  :root {
    --page-bg: #e4e2df;
    --card-light: #b3b3b3;
    --card-mid: #8f8f8f;
    --card-dark: #666666;
    --band: #2f2b2c;
    --ink-white: #f4f4f4;
    --ink-soft: #e2e2e2;
    --icon-bg: #3a3a3a;
  }
  html, body {
    margin: 0;
    width: 1200px;
    height: 1023px;
    overflow: hidden;
    background: var(--page-bg);
  }
  .card {
    position: absolute;
    left: 100px;
    top: 226px;
    width: 1000px;
    height: 571px;
    border-radius: 4px;
    background: radial-gradient(ellipse at 45% 40%, var(--card-light) 0%, var(--card-mid) 55%, var(--card-dark) 100%);
    box-shadow: 0 18px 40px rgba(0,0,0,0.25);
    overflow: hidden;
    font-family: "Cinzel", serif;
  }
  .band {
    position: absolute;
    left: 0;
    top: 238px;
    width: 100%;
    height: 58px;
    background: var(--band);
  }
  .brand {
    position: absolute;
    left: 60px;
    top: 112px;
    color: var(--ink-white);
    font-weight: 400;
    text-transform: uppercase;
    line-height: 1.15;
  }
  .brand-name { font-size: 40px; letter-spacing: 2px; display: block; }
  .brand-sub { font-size: 24px; letter-spacing: 12px; display: block; padding-left: 34px; }
  .holder {
    position: absolute;
    right: 60px;
    top: 82px;
    text-align: right;
    color: var(--ink-white);
  }
  .holder-name {
    font-size: 46px;
    font-weight: 600;
    font-variant: small-caps;
    letter-spacing: 1px;
    margin: 0;
    line-height: 1;
  }
  .holder-title {
    font-size: 22px;
    font-variant: small-caps;
    letter-spacing: 2px;
    margin: 6px 0 0;
    color: var(--ink-soft);
  }
  .contact {
    position: absolute;
    left: 330px;
    top: 340px;
    margin: 0;
    padding: 0;
    list-style: none;
    color: var(--ink-soft);
  }
  .contact li {
    display: flex;
    align-items: center;
    height: 50px;
    margin-bottom: 16px;
    font-size: 27px;
    text-transform: uppercase;
    letter-spacing: 0.5px;
  }
  .contact .icon {
    width: 32px;
    height: 32px;
    margin-right: 22px;
    flex: none;
  }
</style>
</head>
<body>
  <div class="card">
    <div class="band"></div>

    <div class="brand">
      <span class="brand-name">Ambergate</span>
      <span class="brand-sub">Capital</span>
    </div>

    <div class="holder">
      <p class="holder-name">Dorian Velsky</p>
      <p class="holder-title">Managing Partner</p>
    </div>

    <ul class="contact">
      <li>
        <svg class="icon" viewBox="0 0 32 32" aria-hidden="true">
          <rect width="32" height="32" rx="2" fill="var(--icon-bg)"/>
          <path d="M16 6a6 6 0 0 0-6 6c0 5 6 11 6 11s6-6 6-11a6 6 0 0 0-6-6zm0 8.5a2.5 2.5 0 1 1 0-5 2.5 2.5 0 0 1 0 5z" fill="var(--ink-white)"/>
          <rect x="13" y="24" width="6" height="2" fill="var(--ink-white)"/>
        </svg>
        4190 NE 38th Ter. Ocala, FL 34470
      </li>
      <li>
        <svg class="icon" viewBox="0 0 32 32" aria-hidden="true">
          <rect width="32" height="32" rx="2" fill="var(--icon-bg)"/>
          <rect x="7" y="10" width="18" height="12" rx="2" fill="none" stroke="var(--ink-white)" stroke-width="2"/>
          <rect x="11" y="13" width="10" height="6" fill="var(--ink-white)"/>
        </svg>
        561-347-9162
      </li>
      <li>
        <svg class="icon" viewBox="0 0 32 32" aria-hidden="true">
          <rect width="32" height="32" rx="2" fill="var(--icon-bg)"/>
          <path d="M9 8l14 6-6 2-2 7z" fill="none" stroke="var(--ink-white)" stroke-width="2" stroke-linejoin="round"/>
        </svg>
        talvin47@quorimail.net
      </li>
    </ul>
  </div>
</body>
</html>
```